Pell Nutrition Therapy needs a business card design

I need a business card design for my private practice. Green is my favorite color. I would like the back of the card to include an area for future appointment dates and time. I provide nutrition therapy to individuals, groups and families. I work a lot with adolescents and women who have eating disorders, but also work with athletes.

Reason: I received several new designs and would like to take some time reviewing them.

Target Market(s)

I am working primarily with women, but also men (mostly athletes). I work with a lot of runners. I work with people who are 14-60's.

Industry/Entity Type

Nutrition

Font styles to use
Serif
Sans Serif

Colors
9bcb3c
acd037

Requirements
Nice to have
• I would love to have 'Pell' incorporated into the design since it is my last name. If possible, I'd love to have an actual moon if it looks professional.

A picture of food could also be on the card if it is simple, but not sure how it would look with Pell. I am open to ideas for both Pell and a picture of a food item.

Other font style are fine as long as they are easy to read.

```html
<!DOCTYPE html>
<html lang="en">
<head>
<meta charset="utf-8">
<title>Pell Nutrition Therapy – Business Card</title>
<link href="https://fonts.googleapis.com/css2?family=Fira+Sans:wght@400;500;700&display=swap" rel="stylesheet">
<style>
  :root {
    --page: #e9e9e9;
    --card-green: #9bcb3c;
    --band-yellow: #d2dc22;
    --ink: #2b2f24;
    --ink-soft: #3c4430;
    --accent-dot: #7fa82e;
    --rule: #4a5236;
    --icon-fill: #86b232;
  }
  * { box-sizing: border-box; margin: 0; padding: 0; }
  html, body { width: 1200px; height: 1200px; overflow: hidden; }
  body {
    background: var(--page);
    font-family: "Fira Sans", Arial, sans-serif;
    color: var(--ink);
    position: relative;
  }
  .card {
    position: absolute;
    left: 170px;
    width: 860px;
    height: 491px;
    background: var(--card-green);
    box-shadow: 0 8px 24px rgba(0,0,0,0.12);
    overflow: hidden;
  }
  .card--appointment { top: 84px; }
  .card--contact { top: 625px; }

  .wordmark {
    position: absolute;
    display: flex;
    align-items: center;
    gap: 14px;
    font-weight: 500;
    color: var(--ink);
    white-space: nowrap;
    line-height: 1;
  }
  .wordmark__dot {
    display: block;
    border-radius: 50%;
    background: var(--accent-dot);
    flex: none;
  }
  .card--appointment .wordmark { left: 90px; top: 150px; font-size: 40px; }
  .card--appointment .wordmark__dot { width: 34px; height: 34px; }
  .card--contact .wordmark { left: 60px; top: 170px; font-size: 32px; }
  .card--contact .wordmark__dot { width: 26px; height: 26px; }

  .appointment-band {
    position: absolute;
    left: 0; right: 0;
    top: 250px; height: 200px;
    background: var(--band-yellow);
    font-size: 15px;
    color: var(--ink-soft);
  }
  .appointment-band__label { position: absolute; left: 24px; top: 22px; line-height: 1.2; }
  .field { position: absolute; display: flex; align-items: flex-end; gap: 8px; }
  .field__line { display: block; border-bottom: 1.5px solid var(--rule); height: 1px; }
  .field--appointment { left: 180px; top: 50px; }
  .field--appointment .field__line { width: 560px; }
  .field--dates { left: 420px; top: 102px; }
  .field--dates .field__line { width: 320px; }
  .field--time { left: 470px; top: 152px; }
  .field--time .field__line { width: 270px; }

  .address {
    position: absolute; left: 60px; top: 250px;
    font-size: 19px; line-height: 1.3; color: var(--ink-soft);
  }
  .food-icons {
    position: absolute; left: 640px; top: 64px;
    width: 160px; height: 150px;
    background: var(--icon-fill);
    border-radius: 10px;
  }
  .practitioner { position: absolute; left: 520px; top: 248px; }
  .practitioner__name { font-size: 26px; font-weight: 700; }
  .practitioner__creds { font-size: 14px; color: var(--ink-soft); margin-top: 2px; }
  .contact-list { list-style: none; margin-top: 22px; font-size: 19px; line-height: 1.35; }
  .contact-list li { display: flex; align-items: center; gap: 8px; }
  .contact-list svg { width: 16px; height: 16px; flex: none; }
</style>
</head>
<body>

  <section class="card card--appointment" aria-label="Card back with appointment area">
    <div class="wordmark">
      <span class="wordmark__dot" aria-hidden="true"></span>
      <span class="wordmark__name">Pell Nutrition Therapy</span>
    </div>
    <div class="appointment-band">
      <p class="appointment-band__label">future<br>appointment</p>
      <div class="field field--appointment"><span class="field__line"></span></div>
      <div class="field field--dates"><span>dates</span><span class="field__line"></span></div>
      <div class="field field--time"><span>time</span><span class="field__line"></span></div>
    </div>
  </section>

  <section class="card card--contact" aria-label="Card front with contact details">
    <div class="wordmark">
      <span class="wordmark__dot" aria-hidden="true"></span>
      <span class="wordmark__name">Pell Nutrition Therapy</span>
    </div>
    <p class="address">4471 Maple Hollow Lane<br>Brookfield, TN 37010</p>

    <div class="food-icons" role="img" aria-label="Honeycomb of hexagons with line drawings of foods and a runner"></div>

    <div class="practitioner">
      <p class="practitioner__name">Lena Marlow Pell</p>
      <p class="practitioner__creds">MS, RD, LDN</p>
      <ul class="contact-list">
        <li>
          <svg viewBox="0 0 16 16" aria-hidden="true"><rect x="1" y="1" width="14" height="14" rx="2" fill="#2b2f24"/><path d="M5 4c0 4 3 7 7 7l0-2-2-1-1 1c-1-.5-2-1.5-2.5-2.5l1-1-1-2z" fill="#9bcb3c"/></svg>
          <span>555.201.4470</span>
        </li>
        <li>
          <svg viewBox="0 0 16 16" aria-hidden="true"><rect x="1" y="1" width="14" height="14" rx="2" fill="#2b2f24"/><rect x="5.5" y="3" width="5" height="10" rx="1" fill="#9bcb3c"/></svg>
          <span>555.201.4482</span>
        </li>
        <li>
          <svg viewBox="0 0 16 16" aria-hidden="true"><rect x="1" y="1" width="14" height="14" rx="2" fill="#2b2f24"/><rect x="3.5" y="5" width="9" height="6" fill="none" stroke="#9bcb3c" stroke-width="1.2"/><path d="M3.5 5l4.5 3.5 4.5-3.5" fill="none" stroke="#9bcb3c" stroke-width="1.2"/></svg>
          <span>lpell@examplemail.net</span>
        </li>
      </ul>
    </div>
  </section>

</body>
</html>
```